Law Firm Needs Brochure Redesign Using New Logo

We are a personal injury law firm that does auto injuries and other personal injury cases. We want a new brochure that has our updated logo and information. Instead of gold and black, we want more navy, as matches the new logo. The Auto Liability portion should read: "(required by the state of Arizona in the amounts of $25,000 per person / $50,000 per accident, but a higher amount may be best )." The other information can remain the same. We'd like the brochure to keep the same professional tone as the previous brochure.
Our website is https://www.marbrenlegal.com/.

```html
<!DOCTYPE html>
<html lang="en">
<head>
<meta charset="utf-8">
<title>Marbren Law – Trifold Brochure Design</title>
<link rel="stylesheet" href="https://fonts.googleapis.com/css2?family=Roboto:ital,wght@0,300;0,400;0,500;0,700;1,300;1,400&family=Roboto+Condensed:wght@700&display=swap">
<style>
  :root {
    --navy: #0e2244;
    --navy-soft: #24395b;
    --slate: #58585a;
    --gold: #b08a4e;
    --board: #f2f2f2;
    --white: #ffffff;
    --ink: #3c3c3e;
  }
  * { box-sizing: border-box; margin: 0; padding: 0; }
  html, body { width: 1200px; height: 2318px; overflow: hidden; background: var(--board); }
  body { font-family: "Roboto", Arial, sans-serif; color: var(--ink); }
  .canvas { position: relative; width: 1200px; height: 2318px; overflow: hidden; background: var(--board); }
  .abs { position: absolute; }

  /* brand name block (stands in for logo) */
  .brand { position: absolute; display: flex; align-items: center; gap: 10px; }
  .brand-dot { border-radius: 50%; background: var(--navy); flex: none; }
  .brand-name { font-family: "Roboto", Arial, sans-serif; font-weight: 700; color: var(--navy); letter-spacing: .02em; white-space: nowrap; }

  .btn { position: absolute; height: 18px; border-radius: 9px; background: var(--gold); color: var(--white);
         font-size: 9.5px; line-height: 18px; text-align: center; }

  /* presentation board */
  .corner-block { left: 0; top: 0; width: 344px; height: 540px; background: var(--navy); }
  .sheet-title { left: 735px; top: 326px; font-size: 37px; font-weight: 400; color: var(--navy); letter-spacing: .01em; }
  .sheet-sub { left: 733px; top: 365px; font-family: "Roboto Condensed", "Roboto", sans-serif; font-weight: 700; font-size: 66px; color: var(--gold); letter-spacing: .01em; }
  .spec-label { left: 735px; font-size: 9.5px; font-weight: 700; color: var(--navy); letter-spacing: .03em; }
  .swatch { top: 484px; width: 50px; height: 50px; }
  .font-name { left: 735px; top: 584px; font-size: 36px; color: var(--navy); }

  /* panels */
  .panel { position: absolute; overflow: hidden; }
  .shadow { box-shadow: 8px 8px 10px rgba(0,0,0,.14); }
  .photo { position: absolute; }
  .cover-head { color: var(--white); font-size: 22px; line-height: 27px; text-align: center; font-weight: 400; }
  .cover-tag { color: var(--gold); font-size: 14.5px; line-height: 19px; text-align: center; font-style: italic; font-weight: 300; }

  .stat-over { font-size: 11px; color: var(--white); }
  .stat-num { font-size: 28px; color: var(--gold); font-weight: 500; line-height: 30px; }
  .stat-text { font-size: 12.5px; line-height: 15px; color: var(--white); }
  .promise { font-size: 12.5px; line-height: 15px; color: var(--white); }

  .spine { transform: rotate(-90deg); transform-origin: left top; white-space: nowrap; }
  .spine-address { font-size: 10px; line-height: 12px; color: var(--slate); }

  .section-head { font-size: 22px; line-height: 27px; color: var(--navy); font-weight: 400; }
  .body-copy { font-size: 10.5px; line-height: 13px; color: var(--slate); }
  .tips { left: 237px; top: 1684px; width: 222px; }
  .tip { font-size: 10.6px; line-height: 13px; color: var(--white); margin-bottom: 11px; }
  .lead { color: var(--gold); }
  .coverage { width: 176px; font-size: 10.2px; line-height: 13.5px; color: var(--white); }
  .coverage-icon { width: 30px; height: 30px; }
  .contact { font-size: 10.3px; line-height: 14px; color: var(--navy); }
</style>
</head>
<body>
<div class="canvas">

  <!-- ============ PRESENTATION BOARD ============ -->
  <div class="abs corner-block"></div>

  <!-- single front panel -->
  <div class="panel shadow" style="left:201px; top:63px; width:276px; height:636px; background:var(--white);">
    <div class="brand" style="left:44px; top:46px;">
      <span class="brand-dot" style="width:28px;height:28px;"></span>
      <span class="brand-name" style="font-size:22px;">MARBREN LAW</span>
    </div>
    <div class="photo" role="img" aria-label="Couple sitting on the roof of a white SUV with arms raised, overlooking a mountain valley, tinted navy"
         style="left:0; top:123px; width:276px; height:513px; background:linear-gradient(180deg,#233a5e 0%,#2e4768 45%,#5d6a78 70%,#8a8a88 88%,#9d8f7c 100%);"></div>
    <div class="abs cover-head" style="left:0; top:160px; width:276px;">Protect your family in<br>case of a car accident</div>
    <div class="abs cover-tag" style="left:0; top:224px; width:276px;">A little knowledge and preparation<br>go a long way</div>
    <div class="btn" style="left:88px; top:291px; width:104px;">www.MarbrenLegal.com</div>
  </div>

  <!-- brand sheet -->
  <div class="brand" style="left:583px; top:150px; gap:20px;">
    <span class="brand-dot" style="width:90px;height:90px;"></span>
    <span class="brand-name" style="font-size:56px;">MARBREN LAW</span>
  </div>
  <div class="abs sheet-title">BROCHURE DESIGN</div>
  <div class="abs sheet-sub">TRIFOLD</div>
  <div class="abs spec-label" style="top:463px;">COLORS</div>
  <div class="abs swatch" style="left:735px; background:var(--navy);"></div>
  <div class="abs swatch" style="left:794px; background:var(--slate);"></div>
  <div class="abs swatch" style="left:853px; background:var(--gold);"></div>
  <div class="abs spec-label" style="top:562px;">FONTS</div>
  <div class="abs font-name">ROBOTO</div>

  <!-- ============ OUTSIDE SPREAD ============ -->
  <div class="panel shadow" style="left:203px; top:838px; width:818px; height:636px; background:var(--white);">
    <!-- headers -->
    <div class="brand" style="left:56px; top:46px;">
      <span class="brand-dot" style="width:26px;height:26px;"></span>
      <span class="brand-name" style="font-size:20px;">MARBREN LAW</span>
    </div>
    <div class="brand" style="left:600px; top:50px;">
      <span class="brand-dot" style="width:26px;height:26px;"></span>
      <span class="brand-name" style="font-size:20px;">MARBREN LAW</span>
    </div>

    <!-- middle panel background -->
    <div class="abs" style="left:273px; top:121px; width:270px; height:515px; background:#f3f3f3;"></div>

    <!-- left panel -->
    <div class="photo" role="img" aria-label="Desert canyon road stretching into the distance, tinted navy"
         style="left:0; top:121px; width:273px; height:515px; background:linear-gradient(180deg,#2b3e5c 0%,#2a3d5c 40%,#23385a 60%,#1c3053 100%);"></div>
    <div class="abs" style="left:0; top:392px; width:273px; height:1px; background:rgba(255,255,255,.12);"></div>

    <svg class="abs" style="left:45px; top:166px;" width="52" height="40" viewBox="0 0 52 40" fill="none" stroke="#b08a4e" stroke-width="1.6" stroke-linecap="round">
      <path d="M4 24 L8 16 H20 L24 24 V30 H4 Z"/><circle cx="9" cy="31" r="3"/><circle cx="19" cy="31" r="3"/>
      <path d="M30 14 L36 20 M30 24 H38 M30 32 L36 28 M40 6 L42 14 L48 10 L45 17 L51 20 L44 22"/>
      <path d="M32 10 H50 M32 34 H50"/>
    </svg>
    <div class="abs stat-over" style="left:115px; top:160px;">OVER</div>
    <div class="abs stat-num" style="left:115px; top:175px;">107,000</div>
    <div class="abs stat-text" style="left:115px; top:205px; width:140px;">crashes will happen in the state of Arizona this year.</div>

    <svg class="abs" style="left:50px; top:288px;" width="44" height="40" viewBox="0 0 44 40" fill="none" stroke="#b08a4e" stroke-width="1.6" stroke-linecap="round" stroke-linejoin="round">
      <path d="M6 6 L12 28 H34"/><path d="M12 12 L30 24"/><path d="M16 22 H26 L30 32"/>
      <path d="M34 4 L36 10 L42 8 L38 13 M2 36 H40"/>
    </svg>
    <div class="abs stat-over" style="left:115px; top:285px;">OVER</div>
    <div class="abs stat-num" style="left:115px; top:300px;">700</div>
    <div class="abs stat-text" style="left:115px; top:330px; width:140px;">of them will result in fatalities.</div>

    <div class="abs promise" style="left:52px; top:444px; width:196px;">If we don't win, you don't pay attorney fees. That seems fair to us. Know what's happening with your case, get the answers to your questions and work on getting better with the confidence that you've got an excellent group of people working for you.</div>
    <div class="btn" style="left:55px; top:585px; width:104px;">www.MarbrenLegal.com</div>

    <!-- middle panel spine -->
    <div class="abs spine" style="left:298px; top:612px;">
      <div style="display:flex; align-items:center; gap:8px;">
        <span class="brand-dot" style="width:22px;height:22px;"></span>
        <span class="brand-name" style="font-size:16px;">MARBREN LAW</span>
      </div>
    </div>
    <div class="abs spine spine-address" style="left:352px; top:612px;">4870 W. Canyon Drive Suite B104<br>Phoenix AZ 85031</div>

    <!-- right panel (cover) -->
    <div class="photo" role="img" aria-label="Couple sitting on the roof of a white SUV with arms raised, overlooking a mountain valley, tinted navy"
         style="left:543px; top:121px; width:275px; height:515px; background:linear-gradient(180deg,#233a5e 0%,#2e4768 42%,#5d6a78 68%,#8a8a88 86%,#9d8f7c 100%);"></div>
    <div class="abs cover-head" style="left:543px; top:148px; width:275px;">Protect your family in<br>case of a car accident</div>
    <div class="abs cover-tag" style="left:543px; top:213px; width:275px;">A little knowledge and preparation<br>go a long way</div>
    <div class="btn" style="left:630px; top:281px; width:104px;">www.MarbrenLegal.com</div>
  </div>

  <!-- ============ INSIDE SPREAD ============ -->
  <div class="panel shadow" style="left:203px; top:1563px; width:820px; height:635px; background:var(--white);"></div>

  <!-- panel 1: tips -->
  <div class="photo" role="img" aria-label="Driver's hands on a steering wheel, tinted navy"
       style="left:203px; top:1563px; width:277px; height:635px; background:linear-gradient(180deg,#2a3e5e 0%,#263b5c 50%,#20365a 100%);"></div>
  <div class="abs" style="left:233px; top:1590px; font-size:50px; line-height:56px; color:var(--gold);">10</div>
  <div class="abs" style="left:307px; top:1594px; font-size:22px; line-height:27px; color:var(--white);">Tips to<br>Avoid a Crash</div>
  <div class="abs tips">
    <p class="tip"><span class="lead">Anyone making a left turn must wait for all oncoming traffic to clear before proceeding.</span> Yes, even if the light has turned yellow. Wait to be sure that all traffic has stopped.</p>
    <p class="tip"><span class="lead">When your light turns green,</span> check to be sure that no vehicles are entering the intersection late.</p>
    <p class="tip"><span class="lead">Allow plenty of room between you and the car in front of you.</span> Traffic can stop in an instant, even if you can't see anything ahead.</p>
    <p class="tip"><span class="lead">Avoid being distracted.</span> Teenagers are especially susceptible to losing focus if there are too many friends in the car.</p>
    <p class="tip"><span class="lead">Keep the volume of your radio down and never wear headphones.</span> Cars are very soundproof these days, but you need to be able to hear an ambulance or police siren.</p>
    <p class="tip"><span class="lead">Be especially careful</span> on the weekends and early morning hours.</p>
    <p class="tip"><span class="lead">Don't speed.</span> Speed is a factor in most crashes. Street lights are timed and the freeway has traffic. It's likely you won't get there much faster even if you do speed.</p>
    <p class="tip"><span class="lead">Don't drink and drive.</span> Many cab companies offer a free service to get you home safe.</p>
    <p class="tip"><span class="lead">Use your turn signals.</span> This gives an early warning to vehicles you may not be able to see.</p>
  </div>

  <!-- panel 2: coverage -->
  <div class="abs section-head" style="left:511px; top:1594px;">Have the<br>Right Coverage</div>
  <div class="abs body-copy" style="left:511px; top:1662px; width:210px;">Many people don't know about the different kinds of insurance available. In addition to health insurance, we suggest:</div>
  <div class="photo" role="img" aria-label="Hand signing a form beside stacks of coins and a small blue toy car"
       style="left:480px; top:1714px; width:271px; height:144px; background:linear-gradient(135deg,#c9cfd8 0%,#9aa3ad 45%,#7b6a52 70%,#2f6fb3 100%);"></div>
  <div class="abs" style="left:480px; top:1858px; width:271px; height:340px; background:var(--navy);"></div>

  <svg class="abs coverage-icon" style="left:510px; top:1892px;" viewBox="0 0 30 30" fill="none" stroke="#b08a4e" stroke-width="1.3"><rect x="5" y="3" width="16" height="22" rx="1"/><path d="M9 9h8M9 13h8M9 17h5"/><path d="M16 22l8-8 3 3-8 8h-3z"/></svg>
  <div class="abs coverage" style="left:551px; top:1890px;"><span class="lead">Auto Liability</span> (required by the state of Arizona in the amounts of $25,000 per person / $50,000 per accident, but a higher amount may be best)</div>

  <svg class="abs coverage-icon" style="left:510px; top:1960px;" viewBox="0 0 30 30" fill="none" stroke="#b08a4e" stroke-width="1.3"><rect x="6" y="5" width="18" height="22" rx="1"/><rect x="11" y="3" width="8" height="4"/><path d="M9 12l2 2 3-3M16 13h5M9 19l2 2 3-3M16 20h5"/></svg>
  <div class="abs coverage" style="left:551px; top:1958px;"><span class="lead">Uninsured or Underinsured Motorist Coverage.</span> This protects YOU when the other driver doesn't have insurance or not enough.</div>

  <svg class="abs coverage-icon" style="left:510px; top:2028px;" viewBox="0 0 30 30" fill="none" stroke="#b08a4e" stroke-width="1.3"><circle cx="15" cy="8" r="4"/><path d="M7 27v-7a8 8 0 0 1 16 0v7z"/><path d="M15 17v6M12 20h6"/></svg>
  <div class="abs coverage" style="left:551px; top:2027px;"><span class="lead">Medical Payments Coverage.</span> Up to $5,000 in coverage will be paid out to you no matter who is at fault in an accident and does not need to be reimbursed.</div>

  <svg class="abs coverage-icon" style="left:508px; top:2110px;" viewBox="0 0 30 30" fill="none" stroke="#b08a4e" stroke-width="1.3"><path d="M3 14L14 5l11 9"/><path d="M6 12v13h15V12"/><rect x="11" y="17" width="5" height="8"/><path d="M20 20l3 3 5-6"/></svg>
  <div class="abs coverage" style="left:551px; top:2110px;"><span class="lead">Homeowners / Renters Insurance.</span> Protects you in case of injuries on your property as well as damage to your home from covered events.</div>

  <!-- panel 3: safe behavior -->
  <div class="abs section-head" style="left:776px; top:1589px;">Model Safe<br>Behavior</div>
  <div class="abs body-copy" style="left:776px; top:1657px; width:220px;">Always buckle up. Always put your children in car seats/boosters that are rated for their height and weight.</div>
  <div class="photo" role="img" aria-label="Smiling woman fastening her seatbelt in the driver's seat of a car"
       style="left:751px; top:1714px; width:272px; height:144px; background:linear-gradient(135deg,#3a3f48 0%,#6f7883 40%,#c8ccd2 65%,#4a5260 100%);"></div>
  <div class="abs" style="left:751px; top:1858px; width:272px; height:185px; background:var(--navy);"></div>
  <div class="abs section-head" style="left:776px; top:1884px; color:var(--gold);">Never Text While<br>Driving</div>
  <div class="abs body-copy" style="left:776px; top:1952px; width:222px; color:var(--white);">Studies have shown that texting while driving is as dangerous as driving intoxicated.</div>
  <div class="abs body-copy" style="left:776px; top:1991px; width:222px; color:var(--gold); font-style:italic; font-weight:500;">Show your children that no text is more important than your safety. It can wait.</div>

  <div class="abs contact" style="left:776px; top:2066px;">
    <div style="font-weight:700; font-size:12px; line-height:15px;">Marbren Law Group</div>
    4870 W. Canyon Drive Suite B104<br>Phoenix AZ 85031<br>602.555.0147<br>info@MarbrenLegal.com
  </div>
  <span class="abs brand-dot" style="left:940px; top:2072px; width:54px; height:54px;"></span>
  <div class="btn" style="left:833px; top:2156px; width:104px;">www.MarbrenLegal.com</div>

</div>
</body>
</html>
```